Corvane Capital - Website Design

We need a website design for a new commercial real estate company called Corvane Capital. We're effectively commercial mortgage brokers connecting real estate investors to lenders. We need a website that is simple (not busy), elegant, professional, and user-friendly. A lot of the users will be in their 50's and less tech savvy, so a stream-lined design is best. The website will serve as a portal for lenders to review new financing opportunities, as well as for real estate investors to review terms from lenders.
Just uploaded our logo.
Target Market(s)
Commercial real estate investors and lenders
Industry/Entity Type
Real Estate
Number of Pages Required
1 page
Colors
Designer to choose colors to be used in the design.
Look and feel
Each slider illustrates characteristics of the customer's brand and the style your logo design should communicate.

```html
<!DOCTYPE html>
<html lang="en">
<head>
<meta charset="utf-8">
<title>Corvane Capital</title>
<link href="https://fonts.googleapis.com/css2?family=Open+Sans:wght@400;600;700&family=Roboto:wght@400;500;700&display=swap" rel="stylesheet">
<style>
:root{
  --blue:#29a9e1;
  --blue-dark:#1b7fb8;
  --orange:#e07f22;
  --ink:#222;
  --text:#777;
  --line:#ddd;
  --footer:#1f1f1f;
  --white:#fff;
}
*{box-sizing:border-box;margin:0;padding:0}
html,body{width:1200px;height:3180px;overflow:hidden}
body{position:relative;font-family:"Open Sans",sans-serif;color:var(--text);background:var(--white)}
.abs{position:absolute}
h1,h2,h3,h4{font-family:"Roboto",sans-serif;color:var(--ink)}
/* hero */
.hero{position:absolute;left:0;top:0;width:1200px;height:610px;overflow:hidden}
.hero-photo{position:absolute;inset:0;background:linear-gradient(120deg,#c99b5a 0%,#4a6a8a 30%,#2c4e78 60%,#5a86b4 100%)}
.hero-shade{position:absolute;inset:0;background:rgba(10,25,45,.35)}
.brand{position:absolute;left:97px;top:46px;font-family:"Open Sans",sans-serif;font-weight:700;font-size:23px;color:var(--white);letter-spacing:.3px}
.topbar{position:absolute;right:97px;top:16px;display:flex;align-items:center;gap:22px;color:var(--white);font-size:13px;font-weight:600}
.topbar .call b{font-size:19px;font-weight:600}
.btn-outline{border:2px solid var(--white);border-radius:22px;color:var(--white);font-weight:700;font-size:13px;display:inline-flex;align-items:center;gap:7px}
.topbar .btn-outline{padding:7px 16px}
.nav{position:absolute;right:97px;top:68px;display:flex;gap:26px;font-family:"Roboto",sans-serif;font-weight:500;font-size:16px;color:var(--white)}
.nav .on{color:var(--orange)}
.hero-title{position:absolute;top:160px;width:100%;text-align:center;color:var(--white);font-size:60px;font-weight:700;letter-spacing:.5px}
.hero-sub{position:absolute;top:236px;left:0;width:100%;text-align:center;color:var(--white);font-size:19px;line-height:29px}
.hero .btn-outline{position:absolute;left:507px;top:322px;width:184px;height:46px;justify-content:center;font-size:15px;font-family:"Roboto",sans-serif}
.dots{position:absolute;top:444px;left:568px;display:flex;gap:5px}
.dots i{width:12px;height:12px;border:2px solid var(--white);border-radius:50%}
.dots i.on{background:var(--white)}
.hero-curve{position:absolute;left:0;top:500px;width:1200px;height:112px}
/* welcome */
.sec-title{position:absolute;width:100%;text-align:center;font-size:29px;font-weight:700}
.welcome-text{position:absolute;top:672px;left:190px;width:820px;text-align:center;font-size:13.5px;line-height:27px}
.services{position:absolute;top:768px;left:97px;display:flex;gap:23px}
.service{width:234px;height:252px;border:2px solid var(--blue);text-align:center;padding-top:28px}
.service .ico{width:98px;height:98px;border-radius:50%;background:#efefef;margin:0 auto;display:flex;align-items:center;justify-content:center}
.service h3{font-size:18px;font-weight:500;margin:22px 0 10px}
.service p{font-size:12.5px;line-height:21px;padding:0 30px}
/* audience */
.audience{position:absolute;top:1102px;left:0;width:1200px;height:324px;display:flex}
.aud{width:600px;height:100%;position:relative;overflow:hidden}
.aud.borrow{background:linear-gradient(100deg,#2aa3db,#5fc1ea)}
.aud.lend{background:linear-gradient(100deg,#3a3a3a,#5b5753)}
.aud .photo{position:absolute;right:0;top:0;width:60%;height:100%;opacity:.25}
.aud.borrow .photo{background:linear-gradient(90deg,transparent,#e9c6a6)}
.aud.lend .photo{background:linear-gradient(90deg,transparent,#b18d6a)}
.aud svg.icon{position:absolute;left:100px;top:50px}
.aud h2{position:absolute;left:222px;top:62px;color:var(--white);font-size:30px;font-weight:500;letter-spacing:.5px}
.aud p{position:absolute;left:222px;top:116px;width:365px;color:var(--white);font-size:13.5px;line-height:26px}
.aud .btn-outline{position:absolute;left:222px;top:210px;width:200px;height:46px;justify-content:center;font-size:14.5px;font-family:"Roboto",sans-serif}
/* blog */
.posts{position:absolute;top:1569px;left:97px;display:flex;gap:32px}
.post{width:313px}
.post .thumb{position:relative;height:211px}
.post:nth-child(1) .thumb{background:linear-gradient(135deg,#cfd6dc,#8aa4bd)}
.post:nth-child(2) .thumb{background:linear-gradient(135deg,#b9a58a,#5f8aa8)}
.post:nth-child(3) .thumb{background:linear-gradient(135deg,#9a6a4a,#e6e2dc)}
.date{position:absolute;left:-18px;bottom:0;width:58px;height:56px;font-family:"Roboto",sans-serif;color:var(--white);text-align:center}
.date .d{background:var(--orange);height:34px;font-size:18px;font-weight:700;line-height:34px}
.date .m{background:#555;height:22px;font-size:12px;line-height:22px}
.post h3{font-size:19px;font-weight:500;margin:28px 0 10px}
.post p{font-size:12px;line-height:22px;padding-bottom:14px;border-bottom:1px solid var(--line)}
.meta{display:flex;gap:20px;font-size:12px;margin-top:14px;align-items:center}
.meta span{display:flex;align-items:center;gap:6px}
/* calculator */
.calc{position:absolute;top:2014px;left:0;width:1200px;height:424px;overflow:hidden;background:linear-gradient(100deg,#3d3d3d,#6b6b6b 55%,#8a7a6e)}
.calc-shape{position:absolute;left:0;top:0}
.calc h2{position:absolute;left:97px;top:58px;color:var(--white);font-size:31px;line-height:42px;font-weight:500}
.calc .lead{position:absolute;left:97px;top:154px;width:300px;color:var(--white);font-size:13px;line-height:23px}
.calc .more{position:absolute;left:97px;top:248px;color:var(--white);font-family:"Roboto",sans-serif;font-weight:700;font-size:13px}
.row{position:absolute;left:530px;display:flex;align-items:center}
.row label{width:70px;color:var(--white);font-size:13px;line-height:17px}
.track{position:relative;width:262px;height:11px;border-radius:6px;background:#222}
.track .fill{position:absolute;left:0;top:0;height:100%;border-radius:6px;background:var(--blue)}
.track .knob{position:absolute;top:-5px;width:21px;height:21px;border-radius:50%;background:var(--white)}
.field{position:absolute;left:884px;width:216px;height:40px;background:var(--white);font-size:14px;color:#444;padding:11px 12px}
.radios{position:absolute;left:530px;top:2254px;display:flex;gap:34px;color:var(--white);font-size:13px}
.radios span{display:flex;align-items:center;gap:9px}
.radios i{width:15px;height:15px;border-radius:50%;border:2px solid var(--white)}
.radios i.on{border-color:var(--blue);box-shadow:inset 0 0 0 3px #555,inset 0 0 0 7px var(--blue)}
.est{position:absolute;left:530px;top:2290px;color:var(--white);font-size:16px;font-weight:600}
.btn-fill{position:absolute;left:884px;top:2337px;width:140px;height:43px;border-radius:22px;background:var(--orange);color:var(--white);font-family:"Roboto",sans-serif;font-weight:700;font-size:14px;display:flex;align-items:center;justify-content:center;gap:8px}
/* partners */
.partners{position:absolute;top:2584px;left:97px;display:flex;gap:32px}
.partner{width:177px;height:87px;border:1px solid var(--line);display:flex;align-items:center;justify-content:center}
.partner i{display:block;width:120px;height:34px;background:#cfcfcf;border-radius:3px}
/* footer */
.footer-curve{position:absolute;left:0;top:2700px;width:1200px;height:110px}
.footer{position:absolute;left:0;top:2790px;width:1200px;height:390px;background:var(--footer)}
.f-brand{position:absolute;left:97px;top:135px;color:var(--white);font-family:"Open Sans",sans-serif;font-weight:700;font-size:29px;line-height:43px}
.footer h4{position:absolute;top:92px;color:var(--white);font-size:15px;font-weight:500;letter-spacing:.3px}
.links{position:absolute;left:354px;top:128px;list-style:none;color:var(--white);font-size:12px;line-height:19.6px}
.f-text{position:absolute;left:540px;top:128px;width:250px;color:var(--white);font-size:12px;line-height:22px}
.f-input{position:absolute;left:540px;top:181px;width:253px;height:35px;background:var(--white);color:#444;font-size:12px;padding:9px 10px}
.f-btn{position:absolute;left:540px;top:238px;width:102px;height:31px;border-radius:16px;background:var(--orange);color:var(--white);font-size:11px;font-weight:700;text-align:center;line-height:31px}
.contact{position:absolute;left:880px;top:124px;color:var(--white);font-size:12px;line-height:21px}
.contact div{display:flex;gap:18px;margin-bottom:20px}
.contact svg{flex:none;margin-top:4px}
.f-rule{position:absolute;left:97px;top:310px;width:1003px;border-top:1px solid #3a3a3a}
.copy{position:absolute;left:97px;top:338px;color:var(--white);font-size:12px}
.social{position:absolute;left:975px;top:330px;display:flex;gap:9px}
.social i{width:26px;height:26px;border-radius:50%;border:1px solid var(--white)}
</style>
</head>
<body>

<header class="hero">
  <div class="hero-photo" role="img" aria-label="Upward view of glass office towers against a blue sky"></div>
  <div class="hero-shade"></div>
  <div class="brand">CORVANE CAPITAL</div>
  <div class="topbar">
    <span class="call"><svg width="13" height="13" viewBox="0 0 24 24"><path fill="#e07f22" d="M6.6 10.8c1.4 2.8 3.8 5.1 6.6 6.6l2.2-2.2c.3-.3.7-.4 1-.2 1.1.4 2.3.6 3.6.6.6 0 1 .4 1 1V20c0 .6-.4 1-1 1C10.6 21 3 13.4 3 4c0-.6.4-1 1-1h3.5c.6 0 1 .4 1 1 0 1.3.2 2.5.6 3.6.1.3 0 .7-.2 1z"/></svg>&nbsp; CALL US : <b>1 888 888 8888</b></span>
    <span class="btn-outline"><svg width="12" height="12" viewBox="0 0 24 24"><path fill="#fff" d="M3 17.2V21h3.8L17.8 10l-3.8-3.8zM20.7 7c.4-.4.4-1 0-1.4l-2.3-2.3c-.4-.4-1-.4-1.4 0l-1.8 1.8 3.8 3.8z"/></svg>APPLY NOW</span>
  </div>
  <nav class="nav">
    <span class="on">Home</span><span>About Us</span><span>Marketplace</span><span>Borrower</span><span>Lenders</span><span>Resources</span><span>Blog</span><span>Contact</span>
    <svg width="16" height="16" viewBox="0 0 24 24" style="margin-top:2px"><circle cx="10" cy="10" r="6.5" fill="none" stroke="#fff" stroke-width="3"/><path d="M15 15l6 6" stroke="#fff" stroke-width="3"/></svg>
  </nav>
  <h1 class="hero-title">CORVANE CAPITAL</h1>
  <p class="hero-sub">We're effectively commercial mortgage brokers connecting<br>real estate investors to lenders</p>
  <span class="btn-outline">GET A QUOTE</span>
  <div class="dots"><i class="on"></i><i></i><i></i><i></i></div>
  <svg class="hero-curve" viewBox="0 0 1200 112" preserveAspectRatio="none">
    <path d="M0 112 L0 62 Q560 -40 1200 50 L1200 112 Z" fill="#29a9e1"/>
    <path d="M0 112 L0 80 Q560 -20 1200 62 L1200 112 Z" fill="#fff"/>
  </svg>
</header>

<h2 class="sec-title" style="top:614px">WELCOME TO CORVANE CAPITAL</h2>
<p class="welcome-text">At vero eos et accusamus et iusto odio dignissimos ducimus qui blanditiis praesentium voluptatum deleniti atque corrupti quos dolores et quas molestias excepturi sint occaecati cupidit lique sunt in culpa qui officia deserunt.</p>

<section class="services">
  <div class="service">
    <div class="ico"><svg width="46" height="40" viewBox="0 0 46 40"><rect x="3" y="3" width="40" height="34" fill="none" stroke="#e07f22" stroke-width="3"/><rect x="10" y="20" width="5" height="12" fill="#e07f22"/><rect x="18" y="14" width="5" height="18" fill="#e07f22"/><rect x="26" y="10" width="5" height="22" fill="#e07f22"/><rect x="34" y="17" width="4" height="15" fill="#e07f22"/></svg></div>
    <h3>Permanent Financing</h3><p>Nemo enim ipsam voluptatequ ia volu ptas sit asperna</p>
  </div>
  <div class="service">
    <div class="ico"><svg width="44" height="44" viewBox="0 0 44 44"><path d="M36 17A15 15 0 0 0 9 12" fill="none" stroke="#e07f22" stroke-width="6"/><path d="M3 6 L14 6 L6 16 Z" fill="#e07f22"/><path d="M8 27A15 15 0 0 0 35 32" fill="none" stroke="#e07f22" stroke-width="6"/><path d="M41 38 L30 38 L38 28 Z" fill="#e07f22"/></svg></div>
    <h3>Refinance</h3><p>Nemo enim ipsam voluptatequ ia volu ptas sit asperna</p>
  </div>
  <div class="service">
    <div class="ico"><svg width="46" height="40" viewBox="0 0 46 40"><rect x="17" y="2" width="12" height="10" fill="#e07f22"/><rect x="2" y="28" width="12" height="10" fill="#e07f22"/><rect x="17" y="28" width="12" height="10" fill="#e07f22"/><rect x="32" y="28" width="12" height="10" fill="#e07f22"/><path d="M23 12v16M8 28v-8h30v8" fill="none" stroke="#e07f22" stroke-width="2.5"/></svg></div>
    <h3>Acquisition Loans</h3><p>Nemo enim ipsam voluptatequ ia volu ptas sit asperna</p>
  </div>
  <div class="service">
    <div class="ico"><svg width="34" height="44" viewBox="0 0 34 44"><rect x="4" y="2" width="26" height="40" fill="#e07f22"/><g fill="#f2d2b1"><rect x="9" y="7" width="4" height="4"/><rect x="15" y="7" width="4" height="4"/><rect x="21" y="7" width="4" height="4"/><rect x="9" y="15" width="4" height="4"/><rect x="15" y="15" width="4" height="4"/><rect x="21" y="15" width="4" height="4"/><rect x="9" y="23" width="4" height="4"/><rect x="15" y="23" width="4" height="4"/><rect x="21" y="23" width="4" height="4"/><rect x="14" y="32" width="6" height="10"/></g></svg></div>
    <h3>Construction &amp; Bridge</h3><p>Nemo enim ipsam voluptatequ ia volu ptas sit asperna</p>
  </div>
</section>

<section class="audience">
  <div class="aud borrow">
    <div class="photo" role="img" aria-label="Investor working on a laptop"></div>
    <svg class="icon" width="96" height="86" viewBox="0 0 96 86"><g fill="#fff"><circle cx="48" cy="20" r="14"/><path d="M24 76c0-18 10-30 24-30s24 12 24 30z"/><circle cx="20" cy="30" r="10"/><path d="M2 76c0-14 7-24 18-24 4 0 7 1 9 3-5 6-8 13-8 21z"/><circle cx="76" cy="30" r="10"/><path d="M94 76c0-14-7-24-18-24-4 0-7 1-9 3 5 6 8 13 8 21z"/></g></svg>
    <h2>BORROWERS</h2>
    <p>At vero eos et accusamus et iusto odio dignissimos duci mus qui blanditiis praesentium voluptatum deleniti que corrupti quos dolores et quas mol.</p>
    <span class="btn-outline">REQUEST LOAN</span>
  </div>
  <div class="aud lend">
    <div class="photo" role="img" aria-label="Lender reviewing documents at a desk"></div>
    <svg class="icon" width="70" height="86" viewBox="0 0 70 86"><g fill="#fff"><circle cx="35" cy="22" r="18"/><path d="M2 80c0-22 14-36 33-36s33 14 33 36z"/></g></svg>
    <h2>LENDERS</h2>
    <p>At vero eos et accusamus et iusto odio dignissimos duci mus qui blanditiis praesentium voluptatum deleniti que corrupti quos dolores et quas mol.</p>
    <span class="btn-outline">START LENDING</span>
  </div>
</section>

<h2 class="sec-title" style="top:1492px">LATEST BLOG</h2>
<section class="posts">
  <article class="post">
    <div class="thumb" role="img" aria-label="Man smiling while working at a laptop"><div class="date"><div class="d">02</div><div class="m">AUG</div></div></div>
    <h3>Finibus Bonorum et Malorum</h3>
    <p>Nam libero tempore, cum soluta nobis est eligendi optio cumque nihil impedit quo minus id qu..</p>
    <div class="meta"><span><svg width="11" height="11" viewBox="0 0 12 12"><circle cx="6" cy="3.5" r="3" fill="#29a9e1"/><path d="M0 12c0-4 3-5.5 6-5.5s6 1.5 6 5.5z" fill="#29a9e1"/></svg>John Doe</span><span><svg width="13" height="11" viewBox="0 0 14 12"><path d="M1 1h12v7H6l-3 3V8H1z" fill="none" stroke="#29a9e1" stroke-width="1.5"/></svg>3 Comments</span></div>
  </article>
  <article class="post">
    <div class="thumb" role="img" aria-label="Desk with charts, calculator and paperwork"><div class="date"><div class="d">02</div><div class="m">AUG</div></div></div>
    <h3>Finibus Bonorum et Malorum</h3>
    <p>Nam libero tempore, cum soluta nobis est eligendi optio cumque nihil impedit quo minus id qu..</p>
    <div class="meta"><span><svg width="11" height="11" viewBox="0 0 12 12"><circle cx="6" cy="3.5" r="3" fill="#29a9e1"/><path d="M0 12c0-4 3-5.5 6-5.5s6 1.5 6 5.5z" fill="#29a9e1"/></svg>John Doe</span><span><svg width="13" height="11" viewBox="0 0 14 12"><path d="M1 1h12v7H6l-3 3V8H1z" fill="none" stroke="#29a9e1" stroke-width="1.5"/></svg>3 Comments</span></div>
  </article>
  <article class="post">
    <div class="thumb" role="img" aria-label="Hands using a calculator beside a laptop"><div class="date"><div class="d">02</div><div class="m">AUG</div></div></div>
    <h3>Finibus Bonorum et Malorum</h3>
    <p>Nam libero tempore, cum soluta nobis est eligendi optio cumque nihil impedit quo minus id qu..</p>
    <div class="meta"><span><svg width="11" height="11" viewBox="0 0 12 12"><circle cx="6" cy="3.5" r="3" fill="#29a9e1"/><path d="M0 12c0-4 3-5.5 6-5.5s6 1.5 6 5.5z" fill="#29a9e1"/></svg>John Doe</span><span><svg width="13" height="11" viewBox="0 0 14 12"><path d="M1 1h12v7H6l-3 3V8H1z" fill="none" stroke="#29a9e1" stroke-width="1.5"/></svg>3 Comments</span></div>
  </article>
</section>

<section class="calc" role="img" aria-label="Hands typing on a laptop, dimmed behind the loan calculator">
  <svg class="calc-shape" width="600" height="424" viewBox="0 0 600 424">
    <polygon points="0,0 578,0 330,424 290,424 0,240" fill="#e07f22"/>
    <polygon points="0,240 290,424 0,424" fill="#4a4a4a" opacity=".6"/>
  </svg>
  <h2>HOW MUCH WOULD<br>YOU LIKE TO BORROW?</h2>
  <p class="lead">Nemo enim ipsam voluptatem quia volu ptas sit aspernatur aut odit aut fugit, sed quia consequuntur magni.</p>
  <span class="more">READ MORE &gt;&gt;</span>
</section>
<div class="row" style="top:2074px"><label>Loan<br>Amount</label><div class="track"><div class="fill" style="width:65px"></div><div class="knob" style="left:55px"></div></div></div>
<div class="field" style="top:2075px">$20000</div>
<div class="row" style="top:2127px"><label>Interest<br>Rate</label><div class="track"><div class="fill" style="width:30px"></div><div class="knob" style="left:22px"></div></div></div>
<div class="field" style="top:2128px">10%</div>
<div class="row" style="top:2180px"><label>Loan<br>Term</label><div class="track"><div class="fill" style="width:190px"></div><div class="knob" style="left:180px"></div></div></div>
<div class="field" style="top:2181px">7 Years</div>
<div class="radios"><span><i class="on"></i>Monthly</span><span><i></i>Fortnightly</span><span><i></i>Weekly</span></div>
<div class="est">Your Estimated Repayments Would be:</div>
<div class="field" style="top:2284px">$73.98</div>
<div class="btn-fill"><svg width="12" height="12" viewBox="0 0 24 24"><path fill="#fff" d="M3 17.2V21h3.8L17.8 10l-3.8-3.8zM20.7 7c.4-.4.4-1 0-1.4l-2.3-2.3c-.4-.4-1-.4-1.4 0l-1.8 1.8 3.8 3.8z"/></svg>APPLY NOW</div>

<h2 class="sec-title" style="top:2510px">OUR PARTNERS</h2>
<section class="partners">
  <div class="partner"><i></i></div>
  <div class="partner"><i></i></div>
  <div class="partner"><i></i></div>
  <div class="partner"><i></i></div>
  <div class="partner"><i></i></div>
</section>

<svg class="footer-curve" viewBox="0 0 1200 110" preserveAspectRatio="none">
  <path d="M0 0 Q560 110 1200 20 L1200 110 L0 110 Z" fill="#29a9e1"/>
  <path d="M0 20 Q560 125 1200 42 L1200 110 L0 110 Z" fill="#1f1f1f"/>
</svg>
<footer class="footer">
  <div class="f-brand">CORVANE<br>CAPITAL</div>
  <h4 style="left:354px">QUICK LINKS</h4>
  <ul class="links"><li>Home</li><li>About Us</li><li>Marketplace</li><li>Broker</li><li>Lenders</li><li>Resources</li><li>Blog</li><li>Contact</li></ul>
  <h4 style="left:540px">NEWSLETTER SUBSCRIPTION</h4>
  <p class="f-text">Register your Email Address to get Information about us</p>
  <div class="f-input">Email Address</div>
  <div class="f-btn">SUBSCRIBE</div>
  <h4 style="left:880px">CONTACT US</h4>
  <div class="contact">
    <div><svg width="11" height="14" viewBox="0 0 12 16"><path d="M6 0a6 6 0 0 0-6 6c0 4.5 6 10 6 10s6-5.5 6-10a6 6 0 0 0-6-6zm0 8.5A2.5 2.5 0 1 1 6 3.5a2.5 2.5 0 0 1 0 5z" fill="#fff"/></svg><span>Veldweg 12, 4101 AB Harendal<br>Nederland</span></div>
    <div><svg width="12" height="12" viewBox="0 0 24 24"><path fill="#fff" d="M6.6 10.8c1.4 2.8 3.8 5.1 6.6 6.6l2.2-2.2c.3-.3.7-.4 1-.2 1.1.4 2.3.6 3.6.6.6 0 1 .4 1 1V20c0 .6-.4 1-1 1C10.6 21 3 13.4 3 4c0-.6.4-1 1-1h3.5c.6 0 1 .4 1 1 0 1.3.2 2.5.6 3.6.1.3 0 .7-.2 1z"/></svg><span>1 888 888 8888</span></div>
    <div><svg width="13" height="10" viewBox="0 0 14 10"><rect width="14" height="10" fill="#fff"/><path d="M0 0l7 5 7-5" fill="none" stroke="#1f1f1f" stroke-width="1.3"/></svg><span>info@corvanecapital.com</span></div>
  </div>
  <div class="f-rule"></div>
  <div class="copy">Copyrights © 2017, Corvane Capital.&nbsp; All rights reserved.</div>
  <div class="social"><i></i><i></i><i></i><i></i></div>
</footer>

</body>
</html>
```